BrivaTrek Freight Services Business cards

Would like a very unique design catchy but professional for business cards. Please use log provided.Marlon WellsCeo and Founder TransCon Logistix Solutions1-888-913-3225mwells@tlsolutionsus.comwww.bfservicesco.com

```html
<!DOCTYPE html>
<html lang="en">
<head>
<meta charset="utf-8">
<title>BrivaTrek Freight Services – Business Cards</title>
<link rel="stylesheet" href="https://fonts.googleapis.com/css2?family=Lato:ital,wght@0,700;0,900;1,900&display=swap">
<style>
  :root {
    --brand-blue: #1b6fb8;
    --brand-red: #e8202a;
    --card-white: #ffffff;
    --backdrop: #8a6f4e;
    --card-shadow: rgba(0, 0, 0, 0.45);
  }
  * { box-sizing: border-box; margin: 0; padding: 0; }
  html, body {
    width: 900px;
    height: 1200px;
    overflow: hidden;
    background: var(--backdrop);
    font-family: "Lato", Arial, sans-serif;
  }
  .sheet {
    position: relative;
    width: 900px;
    height: 1200px;
  }
  .card {
    position: absolute;
    left: 86px;
    width: 736px;
    height: 428px;
    background: var(--card-white);
    border-radius: 22px;
    overflow: hidden;
    box-shadow: 0 8px 18px var(--card-shadow);
  }
  .card--front { top: 137px; }
  .card--back  { top: 633px; height: 430px; }
  .card__bands {
    position: absolute;
    left: 0;
    top: 0;
    width: 736px;
    height: 430px;
  }
  .band--blue { fill: var(--brand-blue); }
  .band--red  { fill: var(--brand-red); }

  .holder {
    position: absolute;
    left: 38px;
    top: 60px;
  }
  .holder__name {
    font-size: 38px;
    font-weight: 900;
    line-height: 1;
    color: var(--brand-blue);
    letter-spacing: -0.3px;
  }
  .holder__surname { color: var(--brand-red); }
  .holder__role {
    margin-top: 8px;
    font-size: 24px;
    font-weight: 700;
    color: var(--brand-blue);
  }

  .contacts {
    position: absolute;
    left: 37px;
    top: 200px;
    list-style: none;
  }
  .contacts__item {
    display: flex;
    align-items: center;
    height: 34px;
    margin-bottom: 14px;
    font-size: 21px;
    font-weight: 700;
    color: var(--brand-blue);
  }
  .contacts__icon {
    width: 34px;
    height: 34px;
    margin-right: 12px;
    flex: none;
  }
  .contacts__icon circle { fill: var(--brand-red); }
  .contacts__icon .glyph { fill: none; stroke: #fff; stroke-width: 1.8; stroke-linecap: round; stroke-linejoin: round; }
  .contacts__icon .glyph-fill { fill: #fff; }

  .brand-mark {
    position: absolute;
    right: 40px;
    top: 50px;
    width: 300px;
    text-align: right;
    font-size: 40px;
    font-weight: 900;
    line-height: 1.05;
    color: var(--brand-blue);
  }
  .brand-tagline {
    position: absolute;
    right: 38px;
    top: 302px;
    font-size: 21px;
    font-weight: 900;
    font-style: italic;
    color: var(--brand-red);
  }

  .brand-mark--back {
    position: absolute;
    left: 0;
    right: 0;
    top: 105px;
    text-align: center;
    font-size: 50px;
    font-weight: 900;
    line-height: 1.1;
    color: var(--brand-blue);
  }
</style>
</head>
<body>
<main class="sheet">

  <section class="card card--front" aria-label="Business card front">
    <div class="holder">
      <p class="holder__name">Dustin <span class="holder__surname">Harrow</span></p>
      <p class="holder__role">Ceo and Founder</p>
    </div>

    <p class="brand-mark">BrivaTrek<br>Freight Services</p>

    <ul class="contacts">
      <li class="contacts__item">
        <svg class="contacts__icon" viewBox="0 0 34 34" aria-hidden="true">
          <circle cx="17" cy="17" r="17"/>
          <path class="glyph" d="M12 9.5 L14.5 9 L16 13 L14.2 14.4 Q15.5 17.8 19 19.6 L20.4 17.8 L24.5 19.3 L24 22 Q22.5 24.5 19.5 23.8 Q11.5 21 10 13 Q9.8 10.5 12 9.5Z"/>
        </svg>
        1-888-472-6081
      </li>
      <li class="contacts__item">
        <svg class="contacts__icon" viewBox="0 0 34 34" aria-hidden="true">
          <circle cx="17" cy="17" r="17"/>
          <rect class="glyph-fill" x="9" y="11.5" width="16" height="11" rx="1"/>
          <path class="glyph" style="stroke: var(--brand-red); stroke-width:1.4" d="M9.5 12 L17 18 L24.5 12"/>
        </svg>
        dharrow@bfservicesco.com
      </li>
      <li class="contacts__item">
        <svg class="contacts__icon" viewBox="0 0 34 34" aria-hidden="true">
          <circle cx="17" cy="17" r="17"/>
          <circle class="glyph" cx="17" cy="17" r="8" style="fill:none"/>
          <ellipse class="glyph" cx="17" cy="17" rx="3.5" ry="8"/>
          <path class="glyph" d="M9 17 H25 M10.5 13 H23.5 M10.5 21 H23.5"/>
        </svg>
        www.bfservicesco.com
      </li>
    </ul>

    <p class="brand-tagline">BrivaTrek Freight Services</p>

    <svg class="card__bands" viewBox="0 0 736 430" aria-hidden="true">
      <path class="band--blue" d="M0 366 H34 Q42 366 46 358 Q52 350 60 350 H68 Q76 350 82 358 Q86 366 94 366 H736 V396 H0Z"/>
      <rect class="band--red" x="0" y="403" width="736" height="27"/>
    </svg>
  </section>

  <section class="card card--back" aria-label="Business card back">
    <p class="brand-mark--back">BrivaTrek<br>Freight Services</p>

    <svg class="card__bands" viewBox="0 0 736 430" aria-hidden="true">
      <path class="band--blue" d="M0 370 H44 Q52 370 56 362 Q62 354 70 354 H78 Q86 354 92 362 Q96 370 104 370 H650 Q658 370 662 362 Q668 354 676 354 H684 Q692 354 698 362 Q702 370 710 370 H736 V400 H0Z"/>
      <rect class="band--red" x="0" y="407" width="736" height="23"/>
    </svg>
  </section>

</main>
</body>
</html>
```